Quorvex clinic business card - double sided for young clinic

I require business cards for my aesthetic clinic specialising in the below treatments. I would like the cards to be modern as my clinic base are young 22-35 years old. I require my logo on it and would like the edges to be rounded.

I have an aesthetic clinic specialising in :
Quorvex
Lip Enhancement
Chemical Peels
Facial Fillers
Non Surgical Face Lift

I would the cards to have the following information on them:
My logo - (in grey/silver)
address
Phone number
services

Colours :
White/grey/silver and red

a nice image on there, perhaps a set of lips as this is a main service i deliver

Company Name: PDA Address: 52 Farrowmere Road, 4 Brackwell High Street, KT9 4WQ Phone: 0208 794 2160 Website: www.penningtondoweaesthetics.co.uk

Target Market(s)

clinics 22-45 years old mainly female

Industry/Entity Type

Business

Contact Information for Business Card

as above

Requirements
Must have
• logo
• Address
• Email
• Phone number
• Services i offer
Nice to have
• images

```html
<!DOCTYPE html>
<html lang="en">
<head>
<meta charset="utf-8">
<title>Pennington Dowe Aesthetics – Business Card</title>
<link rel="stylesheet" href="https://fonts.googleapis.com/css2?family=Lora:wght@400;500&family=Lato:wght@400&display=swap">
<style>
  :root {
    --page-bg: #e9e9ea;
    --card-white: #ffffff;
    --card-black: #161616;
    --silver: #b4b4b4;
    --silver-dark: #9a9a9a;
    --grey-text: #8a8a8a;
    --rule: #8c8c8c;
    --photo-light: #f6f1ee;
    --photo-warm: #ecdcd3;
  }
  * { box-sizing: border-box; margin: 0; padding: 0; }
  html, body { width: 1200px; height: 900px; overflow: hidden; }
  body {
    background: var(--page-bg);
    font-family: "Lato", Arial, sans-serif;
    position: relative;
  }
  .card {
    position: absolute;
    left: 260px;
    width: 680px;
    height: 388px;
    border-radius: 22px;
    overflow: hidden;
    box-shadow: 0 8px 24px rgba(0,0,0,0.18);
  }
  .card--front { top: 46px; background: var(--card-white); }
  .card--back { top: 466px; background: var(--card-black); text-align: center; }

  .brand-mark {
    width: 92px; height: 92px;
    border-radius: 50%;
    background: var(--silver);
    display: flex; align-items: center; justify-content: center;
  }
  .brand-mark__name {
    font-family: "Lora", Georgia, serif;
    font-size: 32px;
    color: #ffffff;
    letter-spacing: 2px;
  }
  .brand-name__line1 {
    font-family: "Lora", Georgia, serif;
    font-size: 19px;
    letter-spacing: 4px;
    text-transform: uppercase;
  }
  .brand-name__line2 {
    font-family: "Lora", Georgia, serif;
    font-size: 33px;
    letter-spacing: 5px;
    text-transform: uppercase;
    line-height: 1;
  }

  /* Front */
  .front-info { position: absolute; left: 40px; top: 50px; width: 300px; z-index: 1; }
  .front-info .brand-mark { margin-left: 52px; }
  .front-info .brand-name { margin-top: 14px; color: var(--silver-dark); white-space: nowrap; }
  .service-list { list-style: none; margin-top: 10px; color: var(--grey-text); font-size: 17px; line-height: 1.3; }
  .service-list li::before { content: "◆"; font-size: 9px; margin-right: 8px; vertical-align: 3px; }
  .front-photo {
    position: absolute; right: 0; top: 0; width: 400px; height: 100%;
    background: linear-gradient(90deg, var(--card-white) 0%, var(--photo-light) 35%, var(--photo-warm) 100%);
  }

  /* Back */
  .card--back .brand-mark { margin: 38px auto 0; }
  .card--back .brand-mark__name { color: var(--card-black); }
  .card--back .brand-name { margin-top: 12px; color: var(--silver); }
  .contact-row { display: flex; align-items: center; justify-content: center; margin-top: 6px; }
  .contact-row__rule { width: 160px; height: 1px; background: var(--rule); }
  .contact-icon { width: 24px; height: 24px; margin: 0 10px; }
  .contact-text { color: var(--silver); font-size: 17px; letter-spacing: 0.5px; margin-top: 4px; white-space: nowrap; }
  .contact-text--address { color: var(--grey-text); font-size: 18px; }
</style>
</head>
<body>

  <section class="card card--front">
    <div class="front-photo" role="img" aria-label="Clinic treatment photograph"></div>
    <div class="front-info">
      <div class="brand-mark"><span class="brand-mark__name">PDA</span></div>
      <div class="brand-name">
        <div class="brand-name__line1">Pennington Dowe</div>
        <div class="brand-name__line2">Aesthetics</div>
      </div>
      <ul class="service-list">
        <li>Quorvex</li>
        <li>Lip Enhancement</li>
        <li>Chemical Peels</li>
        <li>Facial Fillers</li>
        <li>Non Surgical Face Lift</li>
      </ul>
    </div>
  </section>

  <section class="card card--back">
    <div class="brand-mark"><span class="brand-mark__name">PDA</span></div>
    <div class="brand-name">
      <div class="brand-name__line1">Pennington Dowe</div>
      <div class="brand-name__line2">Aesthetics</div>
    </div>

    <div class="contact-row">
      <span class="contact-row__rule"></span>
      <svg class="contact-icon" viewBox="0 0 24 24" aria-hidden="true">
        <circle cx="12" cy="12" r="10.5" fill="none" stroke="#b4b4b4" stroke-width="1.4"/>
        <path d="M8.5 7.5c.6-.6 1.3-.5 1.7.1l.9 1.5c.3.5.2 1-.2 1.4l-.6.5c.5 1.2 1.5 2.2 2.7 2.7l.5-.6c.4-.4.9-.5 1.4-.2l1.5.9c.6.4.7 1.1.1 1.7-1.2 1.2-3 1-5-.6-1.4-1.1-2.5-2.3-3.3-3.7-1-1.7-.9-2.9.3-3.7z" fill="#b4b4b4"/>
      </svg>
      <span class="contact-row__rule"></span>
    </div>
    <div class="contact-text">0208 794 2160</div>

    <div class="contact-row">
      <span class="contact-row__rule"></span>
      <svg class="contact-icon" viewBox="0 0 24 24" aria-hidden="true">
        <circle cx="12" cy="12" r="10.5" fill="none" stroke="#b4b4b4" stroke-width="1.4"/>
        <circle cx="12" cy="12" r="6" fill="none" stroke="#b4b4b4" stroke-width="1.1"/>
        <ellipse cx="12" cy="12" rx="2.6" ry="6" fill="none" stroke="#b4b4b4" stroke-width="1.1"/>
        <line x1="6" y1="12" x2="18" y2="12" stroke="#b4b4b4" stroke-width="1.1"/>
      </svg>
      <span class="contact-row__rule"></span>
    </div>
    <div class="contact-text">www.penningtondoweaesthetics.co.uk</div>

    <div class="contact-row">
      <span class="contact-row__rule"></span>
      <svg class="contact-icon" viewBox="0 0 24 24" aria-hidden="true">
        <circle cx="12" cy="12" r="10.5" fill="none" stroke="#b4b4b4" stroke-width="1.4"/>
        <path d="M12 6.5a3.8 3.8 0 0 0-3.8 3.8c0 2.8 3.8 7 3.8 7s3.8-4.2 3.8-7A3.8 3.8 0 0 0 12 6.5z" fill="none" stroke="#b4b4b4" stroke-width="1.2"/>
        <circle cx="12" cy="10.3" r="1.3" fill="#b4b4b4"/>
      </svg>
      <span class="contact-row__rule"></span>
    </div>
    <div class="contact-text contact-text--address">52 Farrowmere Road, 4 Brackwell High Street, KT9 4WQ</div>
  </section>

</body>
</html>
```